Kivo4 Website design (Need help to re-design our website)

We need someone to help us re-design our website and launch it. All contents for the website are ready. (Website: https://www.kivo4.com.au/)

-Rearrange categories:
1. Heat Pumps (Link to PALOX site: https://palox.com.au/)
2. Solar (Under the Solar category; remove solar panels, solar inverters, and solar batteries)
3. LED
4. Capability Statement
5. Service and Support
6. Contact us

Home page - redesign but the free quote will stay.

NOTE:
-Try using professional fonts (Example: Helvetica, etc.)
-Try to play with colours related to sustainability, eco-friendliness, solar, energy, and energy efficiency.
-The website's Footer should be readable and use light colour.

Target Market(s)

Residentials & commercial buildings

Industry/Entity Type

SOLAR ENERGY PROVIDER

Coding

Coded - Design and coding required

Colors

Designer to choose colors to be used in the design.

Requirements
Nice to have
• Effects/transition on the words/copy/images.

```html
<!DOCTYPE html>
<html lang="en">
<head>
<meta charset="utf-8">
<title>Kivo4 – Next Generation Energy Saving Products</title>
<link href="https://fonts.googleapis.com/css2?family=Roboto:wght@400;500;700;900&display=swap" rel="stylesheet">
<style>
:root{
  --green:#3a9a35;
  --green-dark:#23701f;
  --green-mid:#2f8a2b;
  --blue:#2236a0;
  --blue-light:#1e88e5;
  --cyan:#1aa3dc;
  --ink:#1d1d1d;
  --muted:#666;
  --footer:#eeeff1;
  --white:#fff;
}
*{box-sizing:border-box;margin:0;padding:0}
html,body{width:1200px;height:4662px;overflow:hidden;background:var(--white)}
body{position:relative;font-family:"Roboto",Helvetica,Arial,sans-serif;color:var(--ink)}
.abs{position:absolute}
a{color:inherit;text-decoration:none}

/* header */
.site-header{position:absolute;left:0;top:0;width:1200px;height:118px;background:var(--white);border-top:3px solid var(--cyan)}
.brand{position:absolute;display:flex;align-items:center;gap:10px}
.brand-mark{width:30px;height:30px;border-radius:50%;background:var(--green)}
.brand-name{font-weight:900;font-size:40px;color:var(--blue);letter-spacing:1px;line-height:1}
.brand-tag{font-size:9px;color:var(--blue);font-weight:500;margin-top:2px}
.btn{position:absolute;display:flex;align-items:center;justify-content:center;border-radius:30px;color:var(--white);font-weight:700;font-size:12px}
.btn-blue{background:linear-gradient(90deg,var(--blue),var(--blue-light))}
.btn-green{background:linear-gradient(90deg,var(--green-dark),var(--green))}
.main-nav{position:absolute;top:78px;left:393px;display:flex;gap:0;font-size:12.5px;font-weight:700;color:#222}
.main-nav span{position:absolute;white-space:nowrap}

/* hero */
.hero{position:absolute;left:0;top:118px;width:1200px;height:624px}
.hero-photo{position:absolute;inset:0;background:linear-gradient(180deg,#6d7f8c 0%,#8d8a7d 35%,#5e6b49 70%,#3f5a26 100%)}
.hero-shade{position:absolute;inset:0;background:rgba(0,0,0,.25)}
.hero-frame{position:absolute;left:232px;top:87px;width:736px;height:405px}
.hero-logo{position:absolute;left:0;width:1200px;top:180px;text-align:center;color:var(--white);font-weight:900;font-size:64px;letter-spacing:2px}
.hero-logo small{display:block;font-size:13px;font-weight:500;letter-spacing:0}
.hero h1{position:absolute;left:0;width:1200px;top:292px;text-align:center;color:var(--white);font-size:35px;font-weight:700;text-shadow:0 2px 6px rgba(0,0,0,.4)}
.hero p{position:absolute;left:0;width:1200px;top:347px;text-align:center;color:var(--white);font-size:22px}

/* eyebrow + headings */
.eyebrow{position:absolute;font-size:18px;font-weight:700;letter-spacing:1.5px;color:var(--green)}
.heading{position:absolute;font-size:42px;font-weight:900;color:var(--ink)}
.center{left:0;width:1200px;text-align:center}

/* about */
.about-copy{position:absolute;left:112px;width:440px;font-size:12.5px;line-height:26px;color:#555}
.checks{position:absolute;left:112px;top:1185px;display:flex;gap:28px;font-size:13px;color:#555}
.checks span{display:flex;align-items:center;gap:8px}
.tick{width:18px;height:18px;border-radius:50%;background:var(--green);display:inline-flex;align-items:center;justify-content:center}
.photo{position:absolute;box-shadow:0 6px 18px rgba(0,0,0,.15)}

/* projects */
.projects{position:absolute;left:0;top:1466px;width:1200px;height:845px;background:linear-gradient(180deg,#2c8a2a,#1f6d1d 60%,#2a7f28)}
.slide{position:absolute}
.slide-caption{position:absolute;left:224px;top:2090px;width:750px;height:64px;background:#1a1a1a;}
.slide-caption span{position:absolute;left:32px;top:20px;color:var(--white);font-size:22px;font-weight:700;border-left:6px solid var(--cyan);padding-left:24px;margin-left:-32px;line-height:34px;top:15px}
.arrow-box{position:absolute;width:56px;height:54px;border:2px solid var(--cyan);display:flex;align-items:center;justify-content:center}
.sq-arrow{position:absolute;width:29px;height:28px;display:flex;align-items:center;justify-content:center;background:var(--cyan)}
.sq-arrow.off{background:#b9e3f4}

/* badges / clients */
.badge{position:absolute;width:156px;height:103px;background:var(--white);box-shadow:0 3px 12px rgba(0,0,0,.14);display:flex;align-items:center;justify-content:center}
.badge-shape{width:70px;height:44px;border-radius:8px;background:#d9e7d6}
.client-name{font-size:20px;font-weight:700;display:flex;align-items:center;gap:8px}
.client-dot{width:16px;height:16px;border-radius:50%}

/* testimonial */
.review-bg{position:absolute;left:0;top:2679px;width:1200px;height:561px;background:linear-gradient(180deg,#fff 0%,#f2f4f1 30%,#b7bdb5 65%,#6f7c63 100%)}
.quote{position:absolute;left:0;width:1200px;top:2840px;text-align:center;font-size:15px;line-height:32px;color:#444}

/* quote form */
.quote-form{position:absolute;left:0;top:3240px;width:1200px;height:498px;background:linear-gradient(180deg,#2a8b28,#3fa23a 60%,#2f8a2b)}
.field{position:absolute;width:315px;height:64px;border-radius:34px;background:var(--white);font-size:13px;color:#666;display:flex;align-items:center;padding-left:34px}
.field .chev{position:absolute;right:22px;top:26px}

/* footer */
.site-footer{position:absolute;left:0;top:4163px;width:1200px;height:499px;background:var(--footer)}
.foot-h{position:absolute;top:4398px;font-size:23px;font-weight:500;color:#222}
.foot-col{position:absolute;top:4444px;font-size:12.5px;line-height:34.5px;color:#666}
</style>
</head>
<body>

<!-- header -->
<header class="site-header">
  <div class="brand" style="left:100px;top:22px">
    <div class="brand-mark"></div>
    <div>
      <div class="brand-name">Kivo4</div>
      <div class="brand-tag">Next Generation Energy Saving Products</div>
    </div>
  </div>
  <a class="btn btn-blue" style="left:816px;top:21px;width:143px;height:34px">Get A Free Quote</a>
  <a class="btn btn-green" style="left:974px;top:21px;width:114px;height:34px">Contact Us</a>
  <nav class="main-nav" style="left:0;top:78px;width:1200px">
    <span style="left:393px">HEAT PUMPS</span>
    <span style="left:509px">SOLAR ⌄</span>
    <span style="left:598px">LED</span>
    <span style="left:655px">CAPABILITY STATEMENT</span>
    <span style="left:843px">SERVICE &amp; SUPPORT</span>
    <span style="left:1006px">CONTACT US</span>
  </nav>
</header>

<!-- hero -->
<section class="hero">
  <div class="hero-photo" role="img" aria-label="Modern home with rooftop solar panels on a lawn, with PALOX 220L and 320L heat pump water tanks"></div>
  <div class="hero-shade"></div>
  <svg class="hero-frame" viewBox="0 0 736 405" fill="none" stroke="#fff" stroke-width="4">
    <path d="M2 110V2H110M626 2H734V110M734 295V403H626M110 403H2V295"/>
  </svg>
  <div class="hero-logo">Kivo4<small>Next Generation Energy Saving Products</small></div>
  <h1>Next Generation Energy Saving Products</h1>
  <p>Save on electricity costs by switching to solar!</p>
  <a class="btn btn-blue" style="left:438px;top:398px;width:165px;height:45px">Get A Free Quote</a>
  <a class="btn btn-green" style="left:625px;top:398px;width:135px;height:45px">Contact Us</a>
  <svg class="abs" style="left:0;top:540px" width="1200" height="84" viewBox="0 0 1200 84">
    <polygon points="0,64 1200,14 1200,84 0,84" fill="#fff"/>
    <polygon points="620,55 1200,20 1200,74" fill="var(--cyan)"/>
    <polygon points="620,55 1200,20 1200,34" fill="#1a78d2"/>
  </svg>
</section>

<!-- about -->
<section class="about">
  <div class="eyebrow" style="left:112px;top:888px">WHO WE ARE</div>
  <div class="heading" style="left:112px;top:922px">ABOUT KIVO4</div>
  <p class="about-copy" style="top:984px">At Kivo4, we trust in our products, our team and our knowledge to ensure the best possible experience when you switch to solar.</p>
  <p class="about-copy" style="top:1062px">Power bills have risen dramatically in Australia over the past decade and energy bills are now among the highest home expenses and business operating expenses for most government, civil and commercial organisations.</p>
  <div class="checks">
    <span><i class="tick"><svg width="10" height="8" viewBox="0 0 10 8"><path d="M1 4l3 3 5-6" stroke="#fff" stroke-width="2" fill="none"/></svg></i>Solar Energy</span>
    <span><i class="tick"><svg width="10" height="8" viewBox="0 0 10 8"><path d="M1 4l3 3 5-6" stroke="#fff" stroke-width="2" fill="none"/></svg></i>LED</span>
    <span><i class="tick"><svg width="10" height="8" viewBox="0 0 10 8"><path d="M1 4l3 3 5-6" stroke="#fff" stroke-width="2" fill="none"/></svg></i>HVAC</span>
  </div>
  <a class="btn btn-blue" style="left:112px;top:1236px;width:105px;height:36px">Read More</a>
  <div class="photo" style="left:599px;top:836px;width:348px;height:395px;background:linear-gradient(160deg,#b7b0a6,#d9d8d4 45%,#6d8a4a)" role="img" aria-label="PALOX heat pump water tanks beside a timber-clad house"></div>
  <div class="photo" style="left:742px;top:1071px;width:344px;height:245px;background:linear-gradient(160deg,#4f6a3c,#cfd3d6 55%,#6f7f57)" role="img" aria-label="Hand holding a phone showing the heat pump control app"></div>
</section>

<!-- projects -->
<section>
  <div class="projects"></div>
  <svg class="abs" style="left:0;top:1466px" width="1200" height="70" viewBox="0 0 1200 70">
    <polygon points="0,0 1200,0 0,64" fill="#fff"/>
    <polygon points="0,0 540,29 0,64" fill="var(--blue)"/>
  </svg>
  <div class="eyebrow center" style="top:1592px;color:var(--cyan)">PROJECTS</div>
  <div class="heading center" style="top:1630px;color:#fff">OUR RECENT PROJECTS</div>
  <div class="slide" style="left:0;top:1719px;width:179px;height:344px;background:linear-gradient(160deg,#8a7155,#cfcfc8 55%,#4d6a35)" role="img" aria-label="Heat pump unit beside a timber wall"></div>
  <div class="slide" style="left:224px;top:1719px;width:750px;height:435px;background:linear-gradient(100deg,#9a6a55 0%,#c9ccd0 30%,#8fa06d 60%,#3f6b2a 100%)" role="img" aria-label="Outdoor air conditioning unit against a brick wall next to a lawn"></div>
  <div class="slide" style="left:224px;top:1980px;width:750px;height:174px;background:linear-gradient(180deg,rgba(0,0,0,0),rgba(0,0,0,.8))"></div>
  <div class="abs" style="left:224px;top:2083px;height:44px;border-left:6px solid var(--cyan);padding-left:26px;color:#fff;font-size:22px;font-weight:700;line-height:44px">400KW (1000+ SOLAR PANELS)</div>
  <div class="slide" style="left:1019px;top:1719px;width:181px;height:344px;background:linear-gradient(160deg,#a6a095,#8d8a82 55%,#4d6a35)" role="img" aria-label="Condenser unit beside siding"></div>
  <div class="arrow-box" style="left:123px;top:2100px"><svg width="20" height="10" viewBox="0 0 20 10"><path d="M19 5H2M6 1L2 5l4 4" stroke="#fff" stroke-width="2" fill="none"/></svg></div>
  <div class="arrow-box" style="left:1021px;top:2100px"><svg width="20" height="10" viewBox="0 0 20 10"><path d="M1 5h17M14 1l4 4-4 4" stroke="#fff" stroke-width="2" fill="none"/></svg></div>
  <a class="btn btn-blue" style="left:525px;top:2194px;width:150px;height:32px">View All Projects</a>
</section>

<!-- accreditations -->
<section>
  <div class="eyebrow" style="left:112px;top:2407px">PARTNERS</div>
  <div class="heading" style="left:112px;top:2442px">ACCREDITATIONS &amp; PARTNERS</div>
  <div class="sq-arrow off" style="left:1001px;top:2433px"><svg width="14" height="8" viewBox="0 0 14 8"><path d="M13 4H2M5 1L2 4l3 3" stroke="#fff" stroke-width="1.6" fill="none"/></svg></div>
  <div class="sq-arrow" style="left:1037px;top:2433px"><svg width="14" height="8" viewBox="0 0 14 8"><path d="M1 4h11M9 1l3 3-3 3" stroke="#fff" stroke-width="1.6" fill="none"/></svg></div>
  <div class="badge" style="left:112px;top:2527px"><div class="badge-shape" style="background:#d7ead5"></div></div>
  <div class="badge" style="left:311px;top:2527px"><div class="badge-shape" style="background:#f1d6d1"></div></div>
  <div class="badge" style="left:510px;top:2527px"><div class="badge-shape" style="background:#dbeecb"></div></div>
  <div class="badge" style="left:709px;top:2527px"><div class="badge-shape" style="background:#d3ecd9"></div></div>
  <div class="badge" style="left:909px;top:2527px"><div class="badge-shape" style="background:#d8d8d8"></div></div>
</section>

<!-- testimonial -->
<section>
  <div class="review-bg" role="img" aria-label="Modern house facade with trees, fading into white"></div>
  <div class="abs" style="left:562px;top:2721px;width:76px;height:76px;border-radius:50%;background:var(--green);display:flex;align-items:center;justify-content:center;color:#fff;font-size:52px;font-weight:900;line-height:1;padding-top:20px">”</div>
  <p class="quote">I am very happy with Kivo4 solar install in my place in Brisbane. Their rates were the most<br>competitive when i shopped around. Their before install and post install process was very smooth. I<br>would recommend going with them.</p>
  <div class="abs" style="left:398px;top:2960px;width:45px;height:45px;border-radius:50%;background:#8a8f96" role="img" aria-label="Reviewer avatar"></div>
  <div class="abs" style="left:460px;top:2960px;font-size:13px;color:#555">Ravi Menon</div>
  <div class="abs" style="left:460px;top:2982px;font-size:10px;color:#777">2 Days ago</div>
  <div class="abs" style="left:597px;top:2955px;width:1px;height:50px;background:#ccc"></div>
  <div class="abs" style="left:640px;top:2965px;font-size:26px;font-weight:500;color:#333">Rateloop</div>
  <div class="sq-arrow" style="left:568px;top:3048px"><svg width="14" height="8" viewBox="0 0 14 8"><path d="M13 4H2M5 1L2 4l3 3" stroke="#fff" stroke-width="1.6" fill="none"/></svg></div>
  <div class="sq-arrow" style="left:603px;top:3048px"><svg width="14" height="8" viewBox="0 0 14 8"><path d="M1 4h11M9 1l3 3-3 3" stroke="#fff" stroke-width="1.6" fill="none"/></svg></div>
  <a class="btn btn-blue" style="left:431px;top:3144px;width:336px;height:34px">DOWNLOAD OUR CAPABILITY STATEMENT</a>
</section>

<!-- quote form -->
<section>
  <div class="quote-form" role="img" aria-label="Green field of solar panels"></div>
  <div class="abs center" style="top:3306px;font-size:19px;font-weight:700;letter-spacing:1.5px;color:#fff">CONTACT US</div>
  <div class="heading center" style="top:3344px;color:#fff">WANT A FREE QUOTE?</div>
  <div class="field" style="left:109px;top:3428px">Full Name *</div>
  <div class="field" style="left:443px;top:3428px">Email Address *</div>
  <div class="field" style="left:777px;top:3428px">Phone Number *</div>
  <div class="field" style="left:109px;top:3519px">Address *</div>
  <div class="field" style="left:443px;top:3519px">I am interested in *<svg class="chev" width="12" height="8" viewBox="0 0 12 8"><path d="M1 1l5 5 5-5" stroke="#333" stroke-width="2" fill="none"/></svg></div>
  <div class="field" style="left:777px;top:3519px">How Did You Find Us *<svg class="chev" width="12" height="8" viewBox="0 0 12 8"><path d="M1 1l5 5 5-5" stroke="#333" stroke-width="2" fill="none"/></svg></div>
  <a class="btn btn-blue" style="left:525px;top:3613px;width:150px;height:36px">Request A Quote</a>
  <svg class="abs" style="left:0;top:3690px" width="1200" height="48" viewBox="0 0 1200 48">
    <polygon points="0,48 1200,10 1200,48" fill="#fff"/>
    <polygon points="280,40 1200,4 1200,22" fill="var(--blue)"/>
  </svg>
</section>

<!-- clients -->
<section>
  <div class="eyebrow center" style="top:3802px">PARTNERS</div>
  <div class="heading center" style="top:3834px">OUR CLIENTS</div>
  <div class="badge" style="left:123px;top:3919px;background:#c8262c"><span class="client-name" style="color:#fff"><i class="client-dot" style="background:#fff"></i>Norvale</span></div>
  <div class="badge" style="left:322px;top:3919px"><span class="client-name" style="color:#1d3f8f"><i class="client-dot" style="background:#1d3f8f;border-radius:3px"></i>Ironhill</span></div>
  <div class="badge" style="left:521px;top:3919px"><span class="client-name" style="color:#1d3570">Courtside</span></div>
  <div class="badge" style="left:720px;top:3919px"><span class="client-name" style="color:#e08a00"><i class="client-dot" style="background:#e08a00"></i>Safewell</span></div>
  <div class="badge" style="left:919px;top:3919px"><span class="client-name" style="color:#d6232a"><i class="client-dot" style="background:#d6232a"></i>Parcelroo</span></div>
  <div class="sq-arrow off" style="left:568px;top:4062px"><svg width="14" height="8" viewBox="0 0 14 8"><path d="M13 4H2M5 1L2 4l3 3" stroke="#fff" stroke-width="1.6" fill="none"/></svg></div>
  <div class="sq-arrow" style="left:603px;top:4062px"><svg width="14" height="8" viewBox="0 0 14 8"><path d="M1 4h11M9 1l3 3-3 3" stroke="#fff" stroke-width="1.6" fill="none"/></svg></div>
</section>

<!-- footer -->
<footer class="site-footer">
  <svg class="abs" style="left:0;top:0" width="1200" height="80" viewBox="0 0 1200 80">
    <polygon points="0,0 1200,0 1200,0" fill="#fff"/>
    <polygon points="0,0 560,36 0,72" fill="var(--cyan)"/>
    <polygon points="0,0 560,36 0,18" fill="#1a78d2"/>
  </svg>
  <div class="brand" style="left:112px;top:112px">
    <div class="brand-mark"></div>
    <div>
      <div class="brand-name">Kivo4</div>
      <div class="brand-tag">Next Generation Energy Saving Products</div>
    </div>
  </div>
  <div class="abs" style="left:548px;top:123px;width:538px;height:50px;border-radius:26px;background:#fff;box-shadow:0 2px 8px rgba(0,0,0,.12);font-size:12px;color:#666;padding:17px 0 0 32px">Enter Email Address</div>
  <a class="btn btn-green" style="left:888px;top:123px;width:198px;height:50px;font-size:13.5px">Subscribe Here</a>
</footer>
<div class="foot-h" style="left:112px">QUICK LINKS</div>
<div class="foot-h" style="left:367px">OFFICES</div>
<div class="foot-h" style="left:704px">CONTACT US</div>
<div class="foot-h" style="left:956px">FOLLOW US</div>
<div class="foot-col" style="left:112px">Home<br>About Us<br>Reviews<br>Contact Us<br>Services &amp; Support</div>
<div class="foot-col" style="left:367px">24 Larkin Street Kensington VIC 3031<br>6A/12 Orchard Drive Nerang QLD 4211<br>9 Foundry Court Irymple VIC 3498<br>305/41 Quayside St, Perth WA 6000<br>4/62 Harbour Street Hobart TAS 7000</div>
<div class="foot-col" style="left:704px">Business hours: 9AM - 5PM<br>1300 555 014<br>enquiries@kivo4.com.au</div>
<div class="foot-col" style="left:956px">Facetrail<br>Tubecast<br>Linkwork</div>
<div class="abs center" style="top:4618px;font-size:12.5px;color:#555">(C) Copyright 2024 | All Rights Reserved</div>

</body>
</html>
```